Lawn maintenance
Greenmoor has you covered!
weekly , biweekly

Target Market(s)

lawn care

Industry/Entity Type

Lawn Care

Contact Information for Business Card

eye catching - not you normal "lawn business" card

Logo Text

Greenmoor Lawncare

Font styles to use
Serif
Sans Serif

Colors
ec1f27
00a990
9bcb3c
0455a3

Requirements
Must have
• Tom Halvik
• 410-555-0187
• Lawn maintenance
• Greenmoor has you covered!
• Call for a quote today!
• weekly or biweekly
Nice to have
• maybe some poker chips or playing cards
Should not have
• snow removal

```html
<!DOCTYPE html>
<html lang="en">
<head>
<meta charset="utf-8">
<title>Greenmoor Lawncare – Business Card</title>
<link rel="stylesheet" href="https://fonts.googleapis.com/css2?family=Cinzel:wght@400;600&display=swap">
<style>
  :root {
    --backdrop: #4a4a4a;
    --card-light: #f2f2f2;
    --card-dark: #000000;
    --brand-green: #2d7d10;
    --leaf-green: #4fa21c;
    --ink: #111111;
    --muted: #555555;
    --white: #ffffff;
  }
  * { margin: 0; padding: 0; box-sizing: border-box; }
  html, body {
    width: 1200px;
    height: 960px;
    overflow: hidden;
    background: var(--backdrop);
    font-family: "Cinzel", "Times New Roman", serif;
  }
  .canvas { position: relative; width: 1200px; height: 960px; }

  .card {
    position: absolute;
    width: 600px;
    height: 342px;
    border-radius: 22px;
    box-shadow: 0 3px 8px rgba(0,0,0,0.45);
  }
  .card--front { left: 302px; top: 119px; background: var(--card-light); }
  .card--back  { left: 299px; top: 498px; background: var(--card-dark); }

  .brand {
    position: absolute;
    display: flex;
    align-items: center;
    gap: 12px;
    font-weight: 600;
    white-space: nowrap;
  }
  .brand__mark { display: block; width: 14px; height: 14px; }
  .card--front .brand { left: 42px; top: 56px; font-size: 31px; color: var(--brand-green); }
  .card--front .brand__mark { background: var(--leaf-green); }
  .card--back .brand { left: 50%; top: 50%; transform: translate(-50%, -50%); font-size: 38px; color: var(--white); }
  .card--back .brand__mark { background: var(--leaf-green); width: 16px; height: 16px; }

  .contact {
    position: absolute;
    left: 362px;
    top: 175px;
    line-height: 1;
  }
  .contact__name  { font-size: 25px; color: var(--brand-green); font-weight: 600; }
  .contact__phone { font-size: 19px; color: var(--ink); margin-top: 4px; }
  .contact__service { font-size: 18px; color: var(--brand-green); font-weight: 600; margin-top: 12px; }
  .contact__lines { margin-top: 5px; font-size: 13px; color: var(--muted); line-height: 16px; }
</style>
</head>
<body>
<main class="canvas">
  <section class="card card--front" aria-label="Business card front">
    <div class="brand"><span class="brand__mark"></span>Greenmoor Lawncare</div>
    <div class="contact">
      <p class="contact__name">Tom Halvik</p>
      <p class="contact__phone">410-555-0187</p>
      <p class="contact__service">Lawn maintenance</p>
      <div class="contact__lines">
        <p>Greenmoor has you covered!</p>
        <p>Call for a quote today!</p>
        <p>weekly or biweekly</p>
      </div>
    </div>
  </section>

  <section class="card card--back" aria-label="Business card back">
    <div class="brand"><span class="brand__mark"></span>Greenmoor Lawncare</div>
  </section>
</main>
</body>
</html>
```